Local Flower Farm Needs Business Card Design

I need business cards designed for a flower farm based in Eudora, Kansas.
Business Info:
We are a local cut flower farm located in Eudora, Kansas, founded by Darla Hoffstrom. What started as a passion for agriculture and search for more joy in daily life has blossomed into a small business dedicated to providing the community with beautiful, fresh, and sustainable flowers. We specialize in local, seasonal blooms, ensuring that every petal reflects the care and dedication we pour into our craft. Our mission is to deliver the highest quality flowers directly to our customers through local farmers markets and to florists who share our commitment to sustainability. Join us in celebrating the beauty of nature, one bloom at a time!
Contact Details:
Darla Hoffstrom
Owner
Phone 913-555-0147
Facebook: Lorabelle Quinn Blossoms
Instagram: @LorabelleQuinnBlossoms
Website: LorabelleQuinnBlossoms.example
Target Market(s)
Wholesale to Florists and Direct to Consumer via Farmers Market
Industry/Entity Type
Florist, Farm
Contact Information for Business Card
Name, Contact Info, Logo
Look and feel

```html
<!DOCTYPE html>
<html lang="en">
<head>
<meta charset="utf-8">
<title>Lorabelle Quinn Blossoms – Business Card</title>
<link rel="stylesheet" href="https://fonts.googleapis.com/css2?family=Libre+Caslon+Text&family=Lato:wght@400&display=swap">
<style>
  :root {
    --teal-deep: #0a2a31;
    --teal-soft: #1d5059;
    --teal-line: #2f5d63;
    --paper: #ffffff;
    --stage: #9b9b9b;
    --bloom-tint: #eef0ef;
    --ink-light: #e8eeee;
  }
  * { margin: 0; padding: 0; box-sizing: border-box; }
  html, body { width: 1093px; height: 1200px; overflow: hidden; }
  body { background: var(--stage); position: relative; font-family: "Lato", sans-serif; }

  .card {
    position: absolute;
    left: 264px;
    width: 578px;
    border-radius: 30px;
    overflow: hidden;
  }
  .card--front { top: 226px; height: 356px; background: var(--paper); }
  .card--back { top: 621px; height: 356px; background: var(--teal-deep); width: 582px; }

  .front__band {
    position: absolute; left: 0; right: 0; bottom: 0; height: 11px;
    background: var(--teal-deep);
  }
  .front__floral {
    position: absolute; left: 0; top: 60px; width: 112px; height: 285px;
    background: linear-gradient(160deg, var(--bloom-tint), rgba(238,240,239,0) 85%);
    border-top-right-radius: 60px;
  }
  .front__accent {
    position: absolute; left: 0; top: 42px; width: 15px; height: 37px;
    background: var(--teal-deep);
  }
  .front__name {
    position: absolute; left: 22px; top: 38px;
    font-family: "Libre Caslon Text", serif; font-size: 21px; line-height: 1;
    color: var(--teal-deep); text-transform: uppercase; letter-spacing: 0.2px;
  }
  .front__role {
    position: absolute; left: 22px; top: 62px;
    font-size: 17px; line-height: 1; color: var(--teal-deep);
  }

  .brand-seal {
    position: absolute; border-radius: 50%;
    display: flex; align-items: center; justify-content: center; text-align: center;
    font-family: "Libre Caslon Text", serif;
  }
  .brand-seal--front {
    left: 342px; top: 23px; width: 182px; height: 182px;
    border: 1px solid var(--teal-line); color: var(--teal-deep);
    font-size: 20px; line-height: 1.25; padding: 20px;
  }
  .brand-seal--back {
    left: 195px; top: 65px; width: 194px; height: 194px;
    border: 1px solid var(--teal-soft); color: var(--teal-soft);
    font-size: 21px; line-height: 1.25; padding: 22px;
  }

  .contact {
    position: absolute; font-size: 17px; line-height: 22px; color: var(--teal-deep);
    display: flex; align-items: center; gap: 5px; white-space: nowrap;
  }
  .contact--left { left: 22px; }
  .contact--right { right: 13px; }
  .contact--row1 { top: 266px; }
  .contact--row2 { top: 292px; }
  .contact__icon { width: 22px; height: 22px; flex: none; }

  .back__web {
    position: absolute; left: 0; right: 0; top: 300px; text-align: center;
    font-size: 17px; letter-spacing: 1.1px; color: var(--ink-light);
  }
</style>
</head>
<body>

<section class="card card--front" aria-label="Business card front">
  <div class="front__floral" role="img" aria-label="Faint line-drawn flower stems"></div>
  <div class="front__accent"></div>
  <h1 class="front__name">Darla Hoffstrom</h1>
  <p class="front__role">Owner</p>

  <div class="brand-seal brand-seal--front">Lorabelle Quinn Blossoms</div>

  <p class="contact contact--left contact--row1">
    <svg class="contact__icon" viewBox="0 0 22 22" aria-hidden="true">
      <circle cx="11" cy="11" r="10.3" fill="none" stroke="#0a2a31" stroke-width="1"/>
      <path d="M7.2 6.3l1.8-.6 1.2 2.4-1.1.9c.5 1.3 1.5 2.3 2.8 2.8l.9-1.1 2.4 1.2-.6 1.8c-.3.6-1 .9-1.7.7-3-.9-5.2-3.1-6.1-6.1-.2-.7.1-1.4.7-1.7z" fill="#0a2a31"/>
    </svg>
    913-555-0147
  </p>
  <p class="contact contact--left contact--row2">
    <svg class="contact__icon" viewBox="0 0 22 22" aria-hidden="true">
      <circle cx="11" cy="11" r="10.3" fill="none" stroke="#0a2a31" stroke-width="1"/>
    </svg>
    Lorabelle Quinn Blossoms
  </p>
  <p class="contact contact--right contact--row1">
    @LorabelleQuinnBlossoms
    <svg class="contact__icon" viewBox="0 0 22 22" aria-hidden="true">
      <circle cx="11" cy="11" r="10.3" fill="none" stroke="#0a2a31" stroke-width="1"/>
    </svg>
  </p>
  <p class="contact contact--right contact--row2">
    LorabelleQuinnBlossoms.example
    <svg class="contact__icon" viewBox="0 0 22 22" aria-hidden="true">
      <circle cx="11" cy="11" r="10.3" fill="none" stroke="#0a2a31" stroke-width="1"/>
      <g fill="none" stroke="#0a2a31" stroke-width="1.1">
        <circle cx="11" cy="11" r="6"/>
        <ellipse cx="11" cy="11" rx="2.6" ry="6"/>
        <path d="M5 11h12M6 8h10M6 14h10"/>
      </g>
    </svg>
  </p>
  <div class="front__band"></div>
</section>

<section class="card card--back" aria-label="Business card back">
  <div class="brand-seal brand-seal--back">Lorabelle Quinn Blossoms</div>
  <p class="back__web">LorabelleQuinnBlossoms.example</p>
</section>

</body>
</html>
```